Business Card for Managing Partner Investment Fund

To create a business card template for an investment fund manager. Business card should be more professional in nature, not too colorful, more upscale, and created using the attached logos and fund name files. I would prefer a black or gray color scheme, but am open to the use of color as well. I would prefer a double sided business card, but open to single sided business card designs as well. The business card should include: name, title, and contact information, as well as logo and company name. I would prefer a more stream-lined, simple business card design.
Updates
Address: 4190 NE 38th Ter. Ocala, FL 34470
Email: talvin47@quorimail.net
Phone: 561-347-9162
Title: managing partner
Name: Dorian Velsky
Fund Name: Ambergate Capital
Logos can be found in files attached to the brief
Target Market(s)
potential investors, other fund managers
Industry/Entity Type
Finance
Contact Information for Business Card
Name on card: Dorian Velsky
Title: Managing Partner
Colors
Designer to choose colors to be used in the design.
Requirements
Must have
- Phone number
- email address
- physical address
- title
- name
- logo
- Fund name
Nice to have
- simple layout
Should not have
- too many colors, busy fonts,

```html
<!DOCTYPE html>
<html lang="en">
<head>
<meta charset="utf-8">
<title>Ambergate Capital — Business Card</title>
<link href="https://fonts.googleapis.com/css2?family=Arimo:wght@400&display=swap" rel="stylesheet">
<style>
  :root {
    --stage: #c8c8c8;
    --card-black: #000000;
    --card-gray: #626262;
    --ink-name: #8c8c8c;
    --ink-title: #9a9a9a;
    --ink-small: #7a7a7a;
    --ink-contact: #8a8a8a;
    --brand: #6e6e6e;
    --bar-left: #3a3a3a;
    --bar-right: #5e5e5e;
  }
  * { margin: 0; padding: 0; box-sizing: border-box; }
  html, body { width: 1200px; height: 1200px; overflow: hidden; }
  body {
    background: var(--stage);
    position: relative;
    font-family: "Arimo", Arial, sans-serif;
  }
  .card {
    position: absolute;
    left: 280px;
    width: 665px;
    height: 368px;
    box-shadow: 4px 6px 8px rgba(0,0,0,0.45);
    overflow: hidden;
  }
  .card--front { top: 20px; background: var(--card-black); }
  .card--back { top: 414px; background: var(--card-black); }
  .card--alt { top: 812px; background: var(--card-gray); }
  .card svg { position: absolute; left: 0; top: 0; }

  .brand-name {
    position: absolute;
    color: var(--brand);
    font-weight: 400;
    text-transform: uppercase;
    letter-spacing: 2px;
    text-align: center;
    line-height: 1.15;
  }
  .card--front .brand-name { left: 16px; top: 62px; width: 196px; font-size: 26px; }
  .emblem .brand-name { left: 0; width: 100%; font-size: 28px; }

  .identity { position: absolute; right: 15px; top: 18px; text-align: right; }
  .identity__name { color: var(--ink-name); font-size: 27px; line-height: 1.1; }
  .identity__title { color: var(--ink-title); font-size: 19px; margin-top: 10px; }
  .identity__company { color: var(--ink-small); font-size: 12px; margin-top: 16px; }

  .contact { position: absolute; left: 15px; top: 260px; list-style: none; }
  .contact li { color: var(--ink-contact); font-size: 14.5px; height: 30px; }
  .contact li:last-child { margin-top: 2px; }

  .emblem { position: absolute; left: 202px; top: 53px; width: 260px; height: 260px; }
  .emblem .brand-name { top: 100px; }
</style>
</head>
<body>

  <section class="card card--front">
    <svg width="665" height="368" viewBox="0 0 665 368">
      <defs>
        <linearGradient id="ringFront" x1="0" y1="0" x2="1" y2="1">
          <stop offset="0" stop-color="#9a9a9a"/>
          <stop offset="0.5" stop-color="#3c3c3c"/>
          <stop offset="1" stop-color="#8a8a8a"/>
        </linearGradient>
        <radialGradient id="portraitFill" cx="0.5" cy="0.4" r="0.6">
          <stop offset="0" stop-color="#ffffff"/>
          <stop offset="1" stop-color="#d6d6d6"/>
        </radialGradient>
      </defs>
      <rect class="divider divider--left" x="16" y="174" width="320" height="20" rx="10" fill="var(--bar-left)"/>
      <rect class="divider divider--right" x="330" y="174" width="320" height="20" rx="10" fill="var(--bar-right)"/>
      <circle class="portrait-ring" cx="332" cy="184" r="56" fill="url(#ringFront)"/>
      <circle cx="332" cy="184" r="50" fill="#111"/>
      <circle class="portrait" cx="332" cy="184" r="48" fill="url(#portraitFill)" role="img" aria-label="Portrait of the managing partner"/>
    </svg>
    <div class="brand-name">Ambergate Capital</div>
    <div class="identity">
      <div class="identity__name">Dorian Velsky</div>
      <div class="identity__title">managing partner</div>
      <div class="identity__company">Ambergate Capital</div>
    </div>
    <ul class="contact">
      <li>talvin47@quorimail.net</li>
      <li>561-347-9162</li>
      <li>4190 NE 38th Ter. Ocala, FL 34470</li>
    </ul>
  </section>

  <section class="card card--back">
    <svg width="665" height="368" viewBox="0 0 665 368">
      <defs>
        <linearGradient id="ringBack" x1="0" y1="0" x2="1" y2="1">
          <stop offset="0" stop-color="#5a5a5a"/>
          <stop offset="0.5" stop-color="#454545"/>
          <stop offset="1" stop-color="#6a6a6a"/>
        </linearGradient>
      </defs>
      <circle class="emblem-ring" cx="332" cy="183" r="130" fill="url(#ringBack)"/>
      <circle cx="332" cy="183" r="110" fill="var(--card-black)"/>
    </svg>
    <div class="emblem"><div class="brand-name">Ambergate Capital</div></div>
  </section>

  <section class="card card--alt">
    <svg width="665" height="368" viewBox="0 0 665 368">
      <defs>
        <radialGradient id="haloAlt" cx="0.5" cy="0.5" r="0.5">
          <stop offset="0.55" stop-color="#1a1a1a" stop-opacity="0.9"/>
          <stop offset="1" stop-color="#626262" stop-opacity="0"/>
        </radialGradient>
        <linearGradient id="ringAlt" x1="0" y1="0" x2="1" y2="1">
          <stop offset="0" stop-color="#6a6a6a"/>
          <stop offset="0.5" stop-color="#2a2a2a"/>
          <stop offset="1" stop-color="#5a5a5a"/>
        </linearGradient>
      </defs>
      <circle class="halo" cx="332" cy="180" r="200" fill="url(#haloAlt)"/>
      <circle class="emblem-ring" cx="332" cy="183" r="130" fill="url(#ringAlt)"/>
      <circle cx="332" cy="183" r="110" fill="var(--card-black)"/>
    </svg>
    <div class="emblem"><div class="brand-name">Ambergate Capital</div></div>
  </section>

</body>
</html>
```